Website design for Australia Equine Insurance business

Website Design Brief
1. Introduction
This brief guides the development of a modern, interactive website for our next-generation equine insurance business. We aim to establish a strong digital presence with a website that embodies innovation, usability, and trust, leading to exceptional user experiences and high customer conversions.

2. Company Background
Our startup offers cutting-edge equine insurance solutions across Australia, leveraging emerging technologies for smarter risk assessment, customer engagement, and claims processing. Our commitment is to protect our customers' financial interests and their equine companions with unparalleled service and modern, flexible insurance options.

3. Objectives
The website should:

Highlight our innovative products, services, and unique value proposition.
Drive lead generation and customer conversion using engaging design elements and compelling CTAs.
Foster customer trust and loyalty through transparency, industry expertise, and interactive features.
Enable users to request quotes, purchase insurance, and file claims online in a seamless, intuitive manner.
Be responsive and user-friendly across all devices.

5. Design Requirements
Look and Feel
The design should reflect our brand's personality: innovative, modern, reliable, and committed to the equine community. It should use our brand colours and logo, ensuring a clean, fresh aesthetic. The style guide should promote consistency across fonts, buttons, form fields, etc.

User Interface
The website should display optimally across desktop, tablet, and mobile, with a focus on usability and accessibility. Clear navigation menus, intuitive search and filters, and easy access to important pages like "Get a Quote," "File a Claim," "Contact Us," etc., should be ensured.

Content
Content should be engaging, easily digestible, and serve to educate users about our unique services and the value of equine insurance. The site should also feature blog posts, video guides, and interactive FAQs to illustrate our industry expertise and the benefits of our next-gen approach.

Functionality
Smart Quote Calculator: An AI-driven quote calculator providing real-time estimates.
Digital Purchase and Claims: Facilitate insurance purchase and claims filing digitally, complemented by AI and blockchain tech for efficiency and transparency.
User Accounts: Customers should be able to manage their policies, payments, and claims through personalized accounts.
AI Chatbot: Implement a chatbot for automated customer support, query resolution, and guidance.
SEO and Analytics: Ensure the website is SEO-optimized and integrated with analytics tools like Google Analytics.
6. Timeline
We aim to complete the website design and development project within a 4-month timeframe, given the startup nature of our business. This includes stages of initial design, content creation, development, testing, and launch.

7. Budget
We understand the importance of investing in quality and are open to reasonable negotiations for ensuring the best output.

Target Market(s)

4. Target Audience Our target audience is tech-savvy horse owners, breeders, trainers, equestrian centres, and younger individuals interested in equine ownership, primarily aged between 18-45. They appreciate digital convenience, technological innovation, and quality service.

Industry/Entity Type

The equine insurance industry is a specialised branch of the broader insurance market, focusing on coverage for all things related to horses. It encompasses a wide range of coverage areas such as mortality insurance (life insurance for horses), medical coverage, loss of use, liability coverage, and more. The industry is one of passion and care, where the clientele often form a deeply emotional connection to their insured assets - their horses. It’s characterized by a strong focus on well-being, safety, and the financial protection of both the horses and their owners. This makes trust, professionalism, and expertise central to any successful equine insurance business. Our new venture is positioned as a next-generation equine insurance provider. This means we are blending traditional insurance offerings with cutting-edge technologies such as AI and machine learning for better risk assessment, seamless customer service, and efficient claims processing. The audience in this sector is diverse, ranging from individual horse owners and breeders to professional trainers and large equestrian centres. Many of our customers have a significant emotional and financial investment in their horses, so they need to feel reassured that their insurance provider understands and respects this. In designing for this industry, it's essential to strike a balance between sophistication and warmth, to reflect both our professional reliability and our understanding of the personal passion that drives our clients. The design needs to feel modern and innovative, signaling our next-gen approach, but also trustworthy and user-friendly, ensuring customers of all technological skill levels feel comfortable using our platform. Moreover, the design should convey a sense of our commitment to the equine community, showing that we're more than just a faceless corporation. We care deeply about the wellbeing of horses and their owners, and we're here to support them with quality insurance solutions tailored to their unique needs.

Coding

Coded - Design and coding required

Number of Pages Required

5+ page

Requirements
Must have
• Responsive Design: The website should be fully responsive, offering optimal viewing and interaction across a range of devices - desktop, tablet, and mobile. Intuitive Navigation: The site should feature an easy-to-understand navigation system that allows users to find the information they're seeking quickly and efficiently. Clear Branding: The design should consistently incorporate the company's logo, colors, and overall aesthetic, reinforcing brand recognition. Content: High-quality, relevant content that explains your services, highlights your unique selling propositions, and educates users about equine insurance. The language should be clear, concise, and engaging. Smart Quote Calculator: An interactive tool enabling potential customers to get real-time insurance quotes. Online Purchase and Claims Filing System: A streamlined, user-friendly process for customers to buy insurance and file claims online. Customer Accounts: A secure area for customers to manage their policies, track claims, and make payments. AI Chatbot: An automated chat feature providing immediate customer support and answering frequently asked questions. SEO Optimization: The site must be search engine friendly, with strategically placed keywords, meta tags, and an XML sitemap for better indexing by search engines. Analytics Integration: Integration with tools like Google Analytics for tracking and analyzing user behavior and site performance. Data Security: Implementation of strong security measures to protect user data, including SSL encryption. Accessibility: Compliance with Web Content Accessibility Guidelines (WCAG) to ensure the site is accessible to people with disabilities. Contact Information: Clearly visible and easily accessible contact details, including phone number, email, and physical address. Social Media Integration: Links to the company's social media profiles for enhanced customer engagement and brand visibility. Remember, while these are essential features, the goal should always be to provide a seamless, positive user experience that aligns with your brand's identity and goals.
Nice to have
• Interactive Features: Interactive elements like quizzes or calculators can engage users, offer value, and make your site more memorable. Video Content: Videos explaining your products, services, or the importance of equine insurance can be a dynamic way to share information and appeal to different learning styles. Live Chat: In addition to an AI chatbot, having a live chat option for immediate customer support could significantly enhance user experience and satisfaction. Personalisation: If your resources allow, personalised content based on user behaviour or preferences can make your website more engaging and relevant. Integrated Blog: A blog section featuring articles on equine health, insurance tips, case studies etc., could help establish your brand as a thought leader in the field and improve SEO. Multilingual Support: If your target audience includes non-English speakers, offering content in multiple languages could be a beneficial feature. Customer Testimonials/Reviews: Including testimonials or reviews from satisfied customers can build trust and offer social proof. Resource Library: A library of downloadable resources (guides, checklists, eBooks) could offer added value to your customers and potential leads. Interactive FAQ: A dynamic FAQ section, where users can find answers quickly, or even an FAQ chatbot, could enhance the user experience. Newsletter Signup: An easily accessible sign-up option for a regular newsletter to keep users informed about your services, industry news, and tips. Integration with Customer Relationship Management (CRM) Software: To manage leads and customer information effectively, if your business operations allow for this level of integration.
Should not have
• Cluttered Layout: Overcrowding pages with too much information, images, or other elements can make your website look messy and confusing, hindering usability. Irrelevant Content: Your website should focus on information that is relevant to your target audience and industry. Avoid including content that does not provide value or enhance understanding of your products or services. Complex Navigation: A website should not have a confusing navigation system. Users should be able to find what they're looking for quickly and easily. Inconsistent Design: Inconsistencies in fonts, colors, or overall design can make your website look unprofessional. The design should be consistent throughout all pages. Slow Loading Times: Large images, animations, or other elements that significantly slow down page loading times should be avoided. Slow websites can lead to a poor user experience and high bounce rates. Poor Mobile Experience: Given the prevalence of mobile browsing, a design that doesn't perform well on mobile devices is a definite no. Autoplay Media: Videos or audio clips that start playing automatically can be annoying to users and should generally be avoided. Inaccessible Content: Ensure that all content is accessible to users of all abilities. Avoid design elements that violate accessibility standards. Hidden Contact Information: Contact information should be easy to find. Do not hide it in obscure parts of the website. Pop-ups: While sometimes necessary for marketing strategies, excessive use of pop-ups can annoy users and distract from the main content. Outdated Plugins: Avoid using outdated plugins or technology that some users may not be able to load or that could pose security risks. Lack of Privacy Policy: A website must have a clear and accessible privacy policy. Not having one can damage trust and may also violate laws or regulations.

```html
<!DOCTYPE html>
<html lang="en">
<head>
<meta charset="utf-8">
<title>Stridewell Equine Insurance</title>
<link href="https://fonts.googleapis.com/css2?family=Bebas+Neue&family=Poppins:wght@400;500;600;700&display=swap" rel="stylesheet">
<style>
:root{
  --navy:#0a2554;
  --navy-deep:#071c43;
  --blue:#0b4cc0;
  --blue-text:#0d4fc4;
  --yellow:#f6b90b;
  --ink:#1b1f2a;
  --muted:#6b7280;
  --light:#f3f4f7;
  --white:#ffffff;
}
*{box-sizing:border-box;margin:0;padding:0}
html,body{width:1200px;height:4928px;overflow:hidden}
body{font-family:'Poppins',sans-serif;color:var(--ink);background:var(--white);position:relative}
.head{font-family:'Bebas Neue',sans-serif;font-weight:400;letter-spacing:.5px;line-height:.95}
.label{font-size:12px;color:var(--blue-text);font-weight:500}
.btn{display:inline-flex;align-items:center;gap:8px;background:var(--yellow);color:var(--ink);font-size:11px;font-weight:700;padding:0 18px;height:36px;border-radius:3px;text-transform:uppercase;letter-spacing:.5px}
.ph{display:block}
section{position:absolute;left:0;width:1200px}
.torn{position:absolute;left:0;width:1200px;height:30px}
p.copy{font-size:12px;line-height:1.7;color:var(--muted)}

/* hero */
.hero{top:0;height:520px;background:linear-gradient(100deg,#2a1c12 0%,#4a3320 45%,#7a5a3a 70%,#3a2a1c 100%)}
.nav{position:absolute;top:20px;left:48px;right:48px;height:40px;display:flex;align-items:center}
.brand{display:flex;align-items:center;gap:8px;color:var(--white);font-weight:700;font-size:18px;letter-spacing:1px}
.brand .dot{width:28px;height:28px;border-radius:50%;background:var(--yellow)}
.menu{display:flex;gap:28px;margin-left:120px;color:var(--white);font-size:10px;font-weight:600;letter-spacing:.5px}
.nav-right{margin-left:auto;display:flex;align-items:center;gap:18px;color:var(--white);font-size:10px;font-weight:600}
.hero h1{position:absolute;left:180px;top:208px;color:var(--white);font-size:60px;width:520px}
.hero .sub{position:absolute;left:180px;top:400px;color:var(--white);font-size:14px;font-weight:500}
.scroll{position:absolute;left:58px;top:470px;transform:rotate(-90deg);transform-origin:left top;color:var(--white);font-size:9px;letter-spacing:2px;font-weight:600}

/* about */
.about{top:520px;height:640px}
.about .photo{position:absolute;left:180px;top:8px;width:300px;height:580px;background:linear-gradient(160deg,#c98a3a,#8a5a2a 55%,#d9b47a)}
.about .bar{position:absolute;left:180px;top:588px;width:300px;height:6px;background:var(--yellow)}
.about .text{position:absolute;left:660px;top:100px;width:440px}
.about h2{font-size:46px;margin:8px 0 16px}
.about h2 span{color:var(--blue-text)}
.checks{display:grid;grid-template-columns:1fr 1fr;gap:10px 20px;margin:18px 0 26px;font-size:11px;font-weight:500}
.checks div{display:flex;align-items:center;gap:8px}
.checks i{width:10px;height:10px;background:var(--blue);border-radius:2px;display:inline-block}

/* benefits */
.benefits{top:1160px;height:560px;background:var(--light)}
.center{text-align:center}
.benefits .titles{position:absolute;top:110px;width:100%}
.benefits h2{font-size:46px;margin-top:6px}
.benefits h2 span,.testi h2 span,.blog h2 span{color:var(--blue-text)}
.circle{position:absolute;top:200px;width:210px;height:210px;border-radius:50%;background:var(--white);box-shadow:0 8px 24px rgba(10,37,84,.1);text-align:center;padding:34px 26px 0}
.circle h3{font-size:12px;font-weight:700;margin:10px 0 6px;line-height:1.3}
.circle p{font-size:9px;line-height:1.5;color:var(--muted)}
.circle .knob{position:absolute;left:93px;bottom:-12px;width:24px;height:24px;border-radius:50%;background:var(--yellow)}

/* services */
.services{top:1700px;height:620px;background:var(--blue)}
.services .label{position:absolute;left:180px;top:72px;color:var(--white)}
.services h2{position:absolute;left:180px;top:92px;color:var(--white);font-size:46px}
.services .btn{position:absolute;left:880px;top:100px}
.card{position:absolute;top:165px;width:256px;height:360px;background:var(--white)}
.card .img{height:160px}
.card .ic{position:absolute;left:108px;top:136px;width:44px;height:44px;border-radius:50%;background:var(--yellow);display:flex;align-items:center;justify-content:center}
.card .body{padding:34px 20px 0;text-align:center}
.card h3{font-size:13px;font-weight:700;margin-bottom:8px}
.card p{font-size:10px;line-height:1.6;color:var(--muted)}
.card .more{margin-top:12px;font-size:10px;font-weight:700;color:var(--blue-text)}

/* quote */
.quote{top:2320px;height:600px}
.quote .left{position:absolute;left:180px;top:170px}
.quote h2{font-size:56px;margin:6px 0 14px}
.quote h2 span{color:var(--blue-text)}
.calc{position:absolute;left:560px;top:-40px;width:640px;height:600px;background:var(--navy);padding:36px 60px}
.calc .label{color:var(--yellow);text-align:center;display:block}
.calc h2{color:var(--white);font-size:44px;text-align:center;margin:4px 0 28px}
.fl{color:var(--white);font-size:11px;font-weight:600;margin:0 0 10px}
.row{display:flex;gap:20px;margin-bottom:16px}
.field{flex:1;height:38px;background:var(--white);border-radius:2px;font-size:11px;color:var(--muted);display:flex;align-items:center;padding:0 12px;justify-content:space-between}
.opts{display:flex;gap:30px;color:var(--white);font-size:11px;margin-bottom:18px}
.opts span{display:flex;align-items:center;gap:6px}
.opts i{width:11px;height:11px;background:var(--white);display:inline-block}
.calc .btn{position:absolute;right:60px;bottom:52px}

/* testimonials */
.testi{top:2920px;height:460px}
.testi .titles{position:absolute;top:22px;width:100%}
.testi h2{font-size:46px;margin-top:6px}
.tcard{position:absolute;top:130px;left:170px;width:860px;height:300px;background:var(--white);box-shadow:0 6px 24px rgba(10,37,84,.1)}
.side{position:absolute;top:150px;width:130px;height:260px;background:var(--white);box-shadow:0 6px 24px rgba(10,37,84,.08)}
.tcard .img{position:absolute;left:20px;top:20px;width:260px;height:260px;background:linear-gradient(160deg,#cbd3dc,#8fa2b6)}
.tcard .q{position:absolute;left:320px;top:30px;color:var(--blue);font-size:70px;font-family:Georgia,serif;line-height:1}
.tcard .txt{position:absolute;left:320px;top:90px;width:500px;font-size:11px;line-height:1.75;color:var(--muted)}
.tcard .name{position:absolute;left:320px;top:232px;font-size:15px;font-weight:700}
.tcard .role{position:absolute;left:320px;top:254px;font-size:10px;color:var(--muted)}
.arrow{position:absolute;top:3200px;width:34px;height:34px;border-radius:50%;background:var(--yellow);display:flex;align-items:center;justify-content:center}

/* blog */
.blog{top:3380px;height:700px}
.blog .label{position:absolute;left:180px;top:18px}
.blog h2{position:absolute;left:180px;top:38px;font-size:46px}
.blog .btn{position:absolute;left:870px;top:42px}
.post{position:absolute;left:180px;top:150px;width:560px}
.post .img{height:240px;background:linear-gradient(150deg,#6b4a30,#3b2a20 50%,#a88a6a)}
.date{font-size:10px;color:var(--muted);margin:16px 0 6px}
.post h3{font-family:'Bebas Neue',sans-serif;font-size:24px;font-weight:400;margin-bottom:8px}
.lm{font-size:10px;font-weight:700;color:var(--blue-text);margin-top:14px}
.aside{position:absolute;left:760px;top:150px;width:250px;border-top:4px solid var(--navy);padding:20px 18px;box-shadow:0 4px 16px rgba(10,37,84,.08);height:470px}
.aside h3{font-family:'Bebas Neue',sans-serif;font-size:20px;font-weight:400;line-height:1.05}
.aside .sep{height:1px;background:#e4e6ec;margin:22px 0}

/* partners */
.partners{top:4080px;height:300px;background:var(--yellow)}
.partners h2{position:absolute;top:90px;width:100%;text-align:center;font-size:26px}
.tile{position:absolute;top:140px;width:150px;height:80px;background:var(--white);display:flex;align-items:center;justify-content:center}
.tile i{width:70px;height:24px;background:#d9dde4;border-radius:3px}

/* newsletter & footer */
.foot{top:4360px;height:568px;background:var(--navy)}
.foot h2{position:absolute;top:62px;width:100%;text-align:center;color:var(--white);font-size:40px}
.news{position:absolute;left:370px;top:124px;width:460px;height:42px;display:flex}
.news .in{flex:1;background:var(--white);font-size:11px;color:var(--muted);display:flex;align-items:center;padding:0 16px}
.news .btn{height:42px;border-radius:0}
.fcol{position:absolute;top:240px;color:#c7d0e2;font-size:11px;line-height:2}
.fcol h4{color:var(--white);font-size:13px;font-weight:600;margin-bottom:8px}
.fcol .brand{font-size:22px;margin-bottom:12px}
.socials{display:flex;gap:8px;margin-top:14px}
.socials i{width:26px;height:26px;border-radius:50%;background:var(--blue);display:block}
.li{display:flex;align-items:center;gap:8px}
.li b{width:5px;height:5px;background:var(--yellow);display:inline-block}
.bottom{position:absolute;left:0;top:520px;width:1200px;height:48px;border-top:1px solid rgba(255,255,255,.15);display:flex;justify-content:space-between;align-items:center;padding:0 180px;color:#c7d0e2;font-size:10px}
</style>
</head>
<body>

<section class="hero">
  <div class="ph" role="img" aria-label="Smiling rider in a blue shirt standing beside his horse in a stable" style="position:absolute;inset:0"></div>
  <nav class="nav">
    <div class="brand"><span class="dot"></span>STRIDEWELL</div>
    <div class="menu"><span>HOME</span><span>ABOUT US</span><span>SERVICES</span><span>GET A QUOTE</span><span>FILE A CLAIM</span><span>RESOURCES</span></div>
    <div class="nav-right"><span>CUSTOMER ACCOUNTS</span><span class="btn" style="height:30px">CONTACT US</span></div>
  </nav>
  <h1 class="head">SAFEGUARDING YOUR HORSES, YOUR PASSION, OUR PRIORITY</h1>
  <div class="sub">Your Partner in Protecting the Health and Well-being of Horses</div>
  <div class="scroll">SCROLL DOWN</div>
  <svg class="torn" style="bottom:-1px" viewBox="0 0 1200 30" preserveAspectRatio="none"><path fill="#fff" d="M0 18 L40 10 L80 20 L130 8 L180 18 L230 6 L290 16 L340 9 L400 19 L460 7 L520 17 L580 10 L640 20 L700 8 L760 18 L820 9 L880 19 L940 7 L1000 17 L1060 9 L1120 18 L1200 8 V30 H0Z"/></svg>
</section>

<section class="about">
  <div class="photo" role="img" aria-label="Young woman gently resting her head against a brown horse"></div>
  <div class="bar"></div>
  <div class="text">
    <div class="label">Welcome to Stridewell Equine Insurance</div>
    <h2 class="head">YOUR TRUSTED EQUINE<br><span>INSURANCE PARTNER</span></h2>
    <p class="copy">Your Partner in Protecting the Health and Well-being of Horses. Our cover is built around the riders, breeders and trainers who care for them every day, with fair terms and quick, clear claims.</p>
    <p class="copy" style="margin-top:10px">We combine long equine experience with smart digital tools, so you can compare cover, manage policies and file a claim online in just a few minutes.</p>
    <div class="checks">
      <div><i></i>Flexible cover options</div><div><i></i>Fast online claims</div>
      <div><i></i>Expert equine support</div><div><i></i>Clear, fair pricing</div>
    </div>
    <span class="btn">LEARN MORE →</span>
  </div>
</section>

<section class="benefits">
  <div class="titles center">
    <div class="label">Our Benefits</div>
    <h2 class="head">BENEFITS OF <span>CHOOSING US</span></h2>
  </div>
  <div class="circle" style="left:275px">
    <svg width="40" height="40" viewBox="0 0 40 40" fill="none" stroke="#0b4cc0" stroke-width="2"><rect x="4" y="4" width="14" height="14"/><rect x="22" y="22" width="14" height="14"/><path d="M18 11h8v11M22 29h-8V18"/></svg>
    <h3>TAILORED COVERAGE FOR YOUR NEEDS</h3>
    <p>Plans shaped around your horse, your riding and your budget.</p>
    <span class="knob"></span>
  </div>
  <div class="circle" style="left:495px">
    <svg width="40" height="40" viewBox="0 0 40 40" fill="none" stroke="#0b4cc0" stroke-width="2"><rect x="8" y="4" width="24" height="32" rx="2"/><path d="M14 14l3 3 6-6M14 24h12M14 30h8"/></svg>
    <h3>EXPERTISE IN EQUINE INSURANCE</h3>
    <p>A team of horse people who understand your world first hand.</p>
    <span class="knob"></span>
  </div>
  <div class="circle" style="left:715px">
    <svg width="40" height="40" viewBox="0 0 40 40" fill="none" stroke="#0b4cc0" stroke-width="2"><circle cx="20" cy="20" r="15"/><path d="M13 20l5 5 9-10"/></svg>
    <h3>SEAMLESS CLAIMS PROCESS</h3>
    <p>Lodge and track every claim online with quick, clear updates.</p>
    <span class="knob"></span>
  </div>
</section>

<section class="services">
  <svg class="torn" style="top:-20px" viewBox="0 0 1200 30" preserveAspectRatio="none"><path fill="#0b4cc0" d="M0 12 L50 20 L110 8 L170 18 L230 6 L300 16 L360 8 L420 20 L480 9 L550 18 L610 6 L680 17 L740 8 L800 19 L870 7 L930 17 L990 9 L1060 20 L1130 8 L1200 16 V30 H0Z"/></svg>
  <div class="label">Our Benefits</div>
  <h2 class="head">WHAT SERVICE WE PROVIDE</h2>
  <span class="btn">VIEW ALL SERVICES →</span>
  <div class="card" style="left:180px">
    <div class="img" role="img" aria-label="Owner walking with a horse" style="background:linear-gradient(150deg,#7a5a3a,#3a2a1c)"></div>
    <span class="ic"><svg width="20" height="20" viewBox="0 0 20 20" fill="none" stroke="#0a2554" stroke-width="2"><path d="M10 2l7 3v5c0 4-3 7-7 8-4-1-7-4-7-8V5z"/></svg></span>
    <div class="body"><h3>EQUINE MORTALITY INSURANCE</h3><p>Protect the value of your horse with cover for death from illness, injury or accident.</p><div class="more">READ MORE →</div></div>
  </div>
  <div class="card" style="left:472px">
    <div class="img" role="img" aria-label="Veterinarian examining a horse" style="background:linear-gradient(150deg,#a8b8c8,#5a6a7a)"></div>
    <span class="ic"><svg width="20" height="20" viewBox="0 0 20 20" fill="none" stroke="#0a2554" stroke-width="2"><path d="M10 3v14M3 10h14"/></svg></span>
    <div class="body"><h3>MEDICAL EXPENSE COVERAGE</h3><p>Help with vet bills, surgery and treatment so care is never a hard choice.</p><div class="more">READ MORE →</div></div>
  </div>
  <div class="card" style="left:764px">
    <div class="img" role="img" aria-label="Insurance policy form on a desk" style="background:linear-gradient(150deg,#9fb8a0,#4f7a6a)"></div>
    <span class="ic"><svg width="20" height="20" viewBox="0 0 20 20" fill="none" stroke="#0a2554" stroke-width="2"><rect x="4" y="2" width="12" height="16"/><path d="M7 7h6M7 11h6"/></svg></span>
    <div class="body"><h3>LIABILITY INSURANCE</h3><p>Cover for damage or injury your horse may cause to people or property.</p><div class="more">READ MORE →</div></div>
  </div>
</section>

<section class="quote">
  <div class="left">
    <div class="label">Get a Quote Today</div>
    <h2 class="head">SECURE YOUR<br><span>EQUINE FUTURE</span></h2>
    <p class="copy" style="margin-bottom:20px">Discover comprehensive equine insurance solutions.</p>
    <span class="btn">GET STARTED →</span>
  </div>
  <div class="calc">
    <span class="label">Calculator</span>
    <h2 class="head">SMART QUOTE CALCULATOR:</h2>
    <div class="fl">Horse Information</div>
    <div class="row"><div class="field">Horse Name</div><div class="field">Select Breed <span>▾</span></div></div>
    <div class="fl">Coverage Options</div>
    <div class="opts"><span><i></i>Mortality</span><span><i></i>Medical Expense Coverage</span><span><i></i>Liability Coverage</span></div>
    <div class="row"><div class="field">Location</div><div class="field">Zip Code</div></div>
    <div class="row"><div class="field">Email</div><div class="field">Phone</div></div>
    <span class="btn">SUBMIT →</span>
  </div>
</section>

<section class="testi">
  <div class="titles center">
    <div class="label">Testimonials</div>
    <h2 class="head">WHAT OUR <span>CUSTOMER SAYS</span></h2>
  </div>
  <div class="side" style="left:-40px"></div>
  <div class="side" style="left:1110px;background:linear-gradient(160deg,#cbd3dc,#8fa2b6)" role="img" aria-label="Portrait of another customer"></div>
  <div class="tcard">
    <div class="img" role="img" aria-label="Portrait of a smiling customer"></div>
    <div class="q">“</div>
    <p class="txt">Your Partner in Protecting the Health and Well-being of Horses made a real difference when our mare fell ill last winter. The team explained every step, the claim was settled within days and we never felt alone. Switching our whole yard over was an easy decision, and the online account makes renewals simple. I happily recommend them to every rider and breeder I know.</p>
    <div class="name">Dana Whitford</div>
    <div class="role">Horse Owner</div>
  </div>
</section>
<div class="arrow" style="left:153px"><svg width="12" height="12" viewBox="0 0 12 12" fill="none" stroke="#0a2554" stroke-width="2"><path d="M8 2L4 6l4 4"/></svg></div>
<div class="arrow" style="left:1013px"><svg width="12" height="12" viewBox="0 0 12 12" fill="none" stroke="#0a2554" stroke-width="2"><path d="M4 2l4 4-4 4"/></svg></div>

<section class="blog">
  <div class="label">Our Blog</div>
  <h2 class="head">LATEST BLOG POST</h2>
  <span class="btn">VIEW ALL BLOGS →</span>
  <div class="post">
    <div class="img" role="img" aria-label="Rider in a stable leading a horse"></div>
    <div class="date">2 Feb 2024</div>
    <h3>CHOOSING THE RIGHT COVERAGE: A GUIDE TO EQUINE INSURANCE OPTIONS</h3>
    <p class="copy">A practical look at the main types of horse cover, what each one pays for and how to match a policy to the way you ride, breed or compete.</p>
    <div class="lm">LEARN MORE →</div>
  </div>
  <div class="aside">
    <div class="date" style="margin-top:0">2 Feb 2024</div>
    <h3>PREPARING FOR THE UNEXPECTED: UNDERSTANDING HORSE INSURANCE CLAIMS</h3>
    <p class="copy" style="margin-top:8px">What to record, who to call and how to lodge a claim quickly.</p>
    <div class="lm">LEARN MORE →</div>
    <div class="sep"></div>
    <div class="date" style="margin-top:0">2 Feb 2024</div>
    <h3>PREPARING FOR THE UNEXPECTED: UNDERSTANDING HORSE INSURANCE CLAIMS</h3>
    <p class="copy" style="margin-top:8px">What to record, who to call and how to lodge a claim quickly.</p>
    <div class="lm">LEARN MORE →</div>
  </div>
</section>

<section class="partners">
  <svg class="torn" style="top:-20px" viewBox="0 0 1200 30" preserveAspectRatio="none"><path fill="#f6b90b" d="M0 14 L60 6 L120 18 L190 8 L250 20 L320 9 L380 17 L450 6 L510 18 L580 9 L640 20 L710 7 L770 17 L840 8 L900 19 L970 9 L1030 18 L1100 6 L1160 16 L1200 10 V30 H0Z"/></svg>
  <h2 class="head">TRUSTED PARTNERS</h2>
  <div class="tile" style="left:195px"><i></i></div>
  <div class="tile" style="left:357px"><i></i></div>
  <div class="tile" style="left:519px"><i></i></div>
  <div class="tile" style="left:681px"><i></i></div>
  <div class="tile" style="left:843px"><i></i></div>
</section>

<section class="foot">
  <h2 class="head">OUR NEWSLETTER</h2>
  <div class="news"><div class="in">Enter your email</div><span class="btn">SUBSCRIBE →</span></div>
  <div class="fcol" style="left:180px;width:220px">
    <div class="brand"><span class="dot"></span>STRIDEWELL</div>
    <div>Smart, caring cover for horses and the people who love them.</div>
    <div class="socials"><i></i><i></i><i></i><i></i></div>
  </div>
  <div class="fcol" style="left:500px">
    <h4>Quick Links</h4>
    <div class="li"><b></b>About Us</div><div class="li"><b></b>Services</div><div class="li"><b></b>Get a quote</div><div class="li"><b></b>File a claim</div><div class="li"><b></b>Resources</div><div class="li"><b></b>Customer Accounts</div>
  </div>
  <div class="fcol" style="left:660px">
    <h4>Services</h4>
    <div class="li"><b></b>Equine Mortality Insurance</div><div class="li"><b></b>Medical Expense Coverage</div><div class="li"><b></b>Liability Insurance</div><div class="li"><b></b>Loss of Use Insurance</div><div class="li"><b></b>Personalized Risk Assessment</div><div class="li"><b></b>Additional Coverage Options</div>
  </div>
  <div class="fcol" style="left:880px">
    <h4>Contact</h4>
    <div>(02) 5550 0148</div><div>12 Paddock Lane, Sampleton</div><div>hello@stridewellequine.com</div>
  </div>
  <div class="bottom"><span>© All Copyright 2024 by STRIDEWELL EQUINE INSURANCE</span><span>All Rights Reserved</span></div>
</section>

</body>
</html>
```